Velmora - 3D medical animations and high end visual content

Our company creates high end visual content and animations for medical global companies.
Our website - www.velmora-studio.example
We would like to have an amazing business card for our CEO that he can use in the following exhebitions he is going to attend.
It is very important that the design will be memorable and diffrent. It has to reflect our brand design (you can have it from our website)
We would like to transmit innovation, prestige, luxury, aesthetics.
The card has to be Double Sided

Target Market(s)

Marketing managers in medical global companys

Industry/Entity Type

It Company

Contact Information for Business Card

Requirements
Nice to have
• It is very important that the design will be memorable and diffrent. It has to reflect our brand design (you can have it from our website)

```html
<!DOCTYPE html>
<html lang="en">
<head>
<meta charset="utf-8">
<title>Velmora – Business Card</title>
<link rel="stylesheet" href="https://fonts.googleapis.com/css2?family=Montserrat:wght@400;500;600&display=swap">
<style>
  :root {
    --backdrop: #2b1c14;
    --card-white: #ffffff;
    --card-black: #050607;
    --ink: #111314;
    --teal: #1b8fa6;
    --rule: #2a2a2a;
    --logo-white: #f4f6f7;
    --logo-rule: #b9c3c7;
  }
  * { box-sizing: border-box; margin: 0; padding: 0; }
  html, body {
    width: 1200px; height: 1000px; overflow: hidden;
    background: var(--backdrop);
    font-family: "Montserrat", Arial, sans-serif;
  }
  .canvas { position: relative; width: 1200px; height: 1000px; }

  .card {
    position: absolute;
    width: 528px; height: 300px;
    box-shadow: 0 8px 24px rgba(0,0,0,.45);
  }

  /* Front side */
  .card--front { left: 70px; top: 230px; background: var(--card-white); color: var(--ink); }
  .brand-mark {
    position: absolute; left: 38px; top: 126px;
    display: flex; align-items: center; gap: 10px;
  }
  .brand-mark__dot { width: 18px; height: 18px; border-radius: 50%; background: var(--teal); }
  .brand-mark__name { font-size: 30px; font-weight: 600; color: var(--ink); letter-spacing: .5px; }

  .identity { position: absolute; left: 262px; top: 60px; }
  .identity__name { font-size: 17px; font-weight: 600; letter-spacing: .5px; }
  .identity__name .surname { color: var(--teal); }
  .identity__title { font-size: 15px; font-weight: 400; margin-top: 4px; }
  .rule--top { position: absolute; left: 262px; right: 0; top: 112px; border-top: 1px solid var(--rule); }
  .rule--mid { position: absolute; left: 262px; width: 170px; top: 148px; border-top: 1px solid var(--rule); }

  .contacts { position: absolute; left: 262px; top: 166px; list-style: none; }
  .contacts li { display: flex; align-items: center; gap: 10px; height: 24px; font-size: 13px; }
  .contacts svg { width: 16px; height: 16px; fill: none; stroke: var(--teal); stroke-width: 1.6; }
  .contacts svg .solid { fill: var(--teal); stroke: none; }

  /* Back side */
  .card--back {
    left: 612px; top: 470px; background: var(--card-black);
    display: flex; align-items: center; justify-content: center;
  }
  .back-wordmark {
    font-size: 42px; font-weight: 500; color: var(--logo-white);
    letter-spacing: 4px; text-transform: uppercase;
  }
</style>
</head>
<body>
<main class="canvas">

  <section class="card card--front" aria-label="Business card front">
    <div class="brand-mark">
      <span class="brand-mark__dot"></span>
      <span class="brand-mark__name">Velmora</span>
    </div>

    <div class="identity">
      <p class="identity__name">LIOR <span class="surname">NAVON</span></p>
      <p class="identity__title">Founder | CEO</p>
    </div>
    <div class="rule--top"></div>
    <div class="rule--mid"></div>

    <ul class="contacts">
      <li>
        <svg viewBox="0 0 16 16" aria-hidden="true"><rect x="4" y="1" width="8" height="14" rx="1.5"/><line x1="7" y1="12.5" x2="9" y2="12.5"/></svg>
        555 - 01 - 4827163
      </li>
      <li>
        <svg viewBox="0 0 16 16" aria-hidden="true"><path class="solid" d="M1 5c0-2 3-3 7-3s7 1 7 3v1.5h-3.5V5H4.5v1.5H1z"/><path class="solid" d="M4 7h8l2 7H2z"/></svg>
        555 - 02 - 9361804
      </li>
      <li>
        <svg viewBox="0 0 16 16" aria-hidden="true"><rect class="solid" x="1" y="3" width="14" height="10"/><path d="M1.5 3.5 8 9l6.5-5.5" stroke="#fff"/></svg>
        lior@velmora-studio.example
      </li>
      <li>
        <svg viewBox="0 0 16 16" aria-hidden="true"><circle cx="8" cy="8" r="6.5"/><ellipse cx="8" cy="8" rx="3" ry="6.5"/><line x1="1.5" y1="8" x2="14.5" y2="8"/></svg>
        www.velmora-studio.example
      </li>
    </ul>
  </section>

  <section class="card card--back" aria-label="Business card back">
    <p class="back-wordmark">Velmora</p>
  </section>

</main>
</body>
</html>
```